Tallow Crest Business Card

We need a business card designed for a a company called "Tallow Crest". We offer consulting, coaching and training to business leaders and coaches (across the world) using the latest findings in neuroscience, social and emotional intelligence and positive psychology. The final design should communicate the use of brain science to create sustainable relationships.

The card should be doublesided. The logo is attached and names and titles will be provided to the successful designer. Thank you.

Industry/Entity Type

Training

```html
<!DOCTYPE html>
<html lang="en">
<head>
<meta charset="utf-8">
<title>Tallow Crest Business Card</title>
<link rel="stylesheet" href="https://fonts.googleapis.com/css2?family=Source+Sans+3:wght@400;700&display=swap">
<style>
  :root {
    --brand-blue: #008fc5;
    --brand-lime: #c2d82b;
    --ink: #111111;
    --paper: #ffffff;
    --edge: #b8b8b8;
  }
  html, body {
    margin: 0;
    padding: 0;
    overflow: hidden;
    background: var(--paper);
  }
  .canvas {
    position: relative;
    width: 1200px;
    height: 1000px;
    background: var(--paper);
    font-family: "Source Sans 3", "Myriad Pro", Arial, sans-serif;
    overflow: hidden;
  }
  .card {
    position: absolute;
    box-sizing: border-box;
    text-align: center;
  }
  .card--front {
    left: 207px;
    top: 220px;
    width: 320px;
    height: 555px;
    border: 2px solid var(--edge);
    background: var(--paper);
  }
  .card--back {
    left: 677px;
    top: 223px;
    width: 314px;
    height: 551px;
    background: var(--brand-blue);
  }
  .wordmark {
    position: absolute;
    left: 0;
    right: 0;
    margin: 0;
    font-weight: 700;
    font-size: 44px;
    line-height: 1;
    letter-spacing: 0.5px;
  }
  .card--front .wordmark { top: 334px; top: 332px; color: var(--brand-blue); transform: translateY(-220px); }
  .card--back .wordmark { top: 262px; color: var(--paper); }
  .contact-band {
    position: absolute;
    left: 0;
    right: 0;
    top: 268px;
    bottom: 0;
    background: var(--brand-lime);
  }
  .person-name {
    position: absolute;
    left: 0; right: 0;
    top: 40px;
    margin: 0;
    font-weight: 400;
    font-size: 24px;
    color: var(--ink);
    line-height: 1;
  }
  .person-role {
    position: absolute;
    left: 0; right: 0;
    top: 67px;
    font-size: 15px;
    color: var(--brand-blue);
    line-height: 1;
  }
  .contact-lines {
    position: absolute;
    left: 0; right: 0;
    top: 107px;
    font-size: 22px;
    line-height: 30px;
    color: var(--ink);
  }
  .divider {
    position: absolute;
    left: 0; right: 0;
    top: 210px;
    height: 2px;
    background: var(--brand-blue);
  }
  .address {
    position: absolute;
    left: 0; right: 0;
    top: 226px;
    font-size: 16px;
    line-height: 21px;
    color: var(--ink);
  }
  .website {
    position: absolute;
    left: 0; right: 0;
    top: 372px;
    font-size: 17px;
    color: var(--paper);
    line-height: 1;
  }
  .side-label {
    position: absolute;
    top: 796px;
    width: 200px;
    margin-left: -100px;
    text-align: center;
    font-size: 24px;
    color: var(--ink);
    line-height: 1;
  }
  .side-label--front { left: 364px; }
  .side-label--back { left: 828px; }
</style>
</head>
<body>
<div class="canvas">
  <section class="card card--front">
    <p class="wordmark">Tallow Crest</p>
    <div class="contact-band">
      <h1 class="person-name">MARA LINDQVIST</h1>
      <div class="person-role">position</div>
      <div class="contact-lines">
        <div>mara@tallowcrest.com</div>
        <div>555.204.7316</div>
      </div>
      <div class="divider"></div>
      <div class="address">
        <div>472 Harbor Bend Way</div>
        <div>Westport, CA 94620-2241</div>
      </div>
    </div>
  </section>
  <div class="side-label side-label--front">front</div>

  <section class="card card--back">
    <p class="wordmark">Tallow Crest</p>
    <div class="website">www.tallowcrest.com</div>
  </section>
  <div class="side-label side-label--back">back</div>
</div>
</body>
</html>
```